Flyer for IT Services

We need a flyer template for our different products and services we offer. We're an IT firm that provides Managed Services, Remote Backup, Mobile Device Management, Unified Communications, and more.

The flyer should be two sided and provide an area for an explanation of the service and then some pictures, lists of features, and a section for our contact info and company description.

We will normally send the flyer over to a client as a PDF via email but may also printer the flyers to hand out at meetings with prospects.

Information on the services to get ideas is at the following and the services heading:
www.fernridgetech.com

Target Market(s)

small to medium sized companies (2-150 employees)

Industry/Entity Type

Printer

Requirements
Must have
• Flyer must be two sided, include our logo, and have sections for product and company description as well as feature lists.

```html
<!DOCTYPE html>
<html lang="en">
<head>
<meta charset="utf-8">
<title>Fern Ridge Technology – IT Services Flyer</title>
<link rel="stylesheet" href="https://fonts.googleapis.com/css2?family=Ubuntu:ital,wght@0,400;0,500;0,700;1,400&family=Arimo:wght@400;700&display=swap">
<style>
  :root{
    --backdrop:#e7e2da;
    --paper:#f7f8f9;
    --blue:#3a9fe6;
    --ink:#3d3d3d;
    --band:#2a2a2a;
    --band-text:#f0f0f0;
    --strip:#e4e4e4;
    --badge-grey:#d5d9dd;
  }
  *{box-sizing:border-box;margin:0;padding:0}
  html,body{width:1200px;height:900px;overflow:hidden}
  body{background:var(--backdrop);position:relative;font-family:"Ubuntu",sans-serif;color:var(--ink)}

  .flyer{position:absolute;top:178px;width:475px;height:612px;background:var(--paper);overflow:hidden;box-shadow:0 2px 8px rgba(0,0,0,.18)}
  .flyer--front{left:75px}
  .flyer--back{left:660px;font-family:"Arimo",sans-serif}

  .brand{position:absolute;left:22px;top:24px;display:flex;align-items:center;gap:10px}
  .brand__dot{width:34px;height:34px;border-radius:50%;background:var(--band)}
  .brand__name{font-size:40px;font-weight:700;color:var(--blue);letter-spacing:2px;line-height:1}

  .tab{position:absolute;left:0;width:4px;height:22px;background:var(--blue)}
  .section-title{position:absolute;left:22px;font-size:18px;font-weight:400;color:var(--blue)}
  .section-copy{position:absolute;left:22px;width:262px;font-size:11.3px;line-height:20.6px;color:var(--ink);text-align:justify;hyphens:auto}
  .section-copy strong{font-weight:700}

  .cta{position:absolute;left:22px;top:421px;width:261px;height:56px;background:var(--blue);border-radius:3px;color:#fff;text-align:center;font-size:19px;line-height:24px;padding-top:4px}
  .cta strong{font-weight:700}

  .hero-photo{position:absolute;left:292px;top:18px;width:183px;height:485px;
    background:linear-gradient(180deg,#f3f5f7 0%,#e9edf1 38%,#8b8e93 52%,#45484d 70%,#2b2c2f 100%)}
  .hero-photo--faint{left:240px;top:20px;width:235px;height:420px;opacity:.14}

  .url-strip{position:absolute;left:0;top:503px;width:475px;height:22px}
  .url-strip svg{position:absolute;left:0;top:0}
  .url{position:absolute;top:3px;font-size:13px;font-weight:700;letter-spacing:1.3px;color:var(--band)}
  .flyer--front .url{left:14px}
  .flyer--back .url{right:14px;font-family:"Ubuntu",sans-serif}
  .footer{position:absolute;left:0;top:525px;width:475px;height:87px;background:var(--band);color:var(--band-text);font-family:"Ubuntu",sans-serif}
  .footer__tagline{position:absolute;left:28px;top:12px;width:175px;text-align:center;font-style:italic;font-size:14px;line-height:22px}
  .footer__rule{position:absolute;left:226px;top:10px;height:66px;border-left:2px dotted #888}
  .footer__contact{position:absolute;left:262px;top:9px;font-size:10.5px;line-height:13px}
  .footer__company{font-size:13px;font-weight:500;margin-bottom:2px}
  .footer__phone{font-weight:700;font-size:9.5px;margin-top:3px}

  .service-bar{position:absolute;left:25px;top:28px;width:424px;height:31px;background:var(--blue);color:#fff;font-size:19px;font-weight:400;padding:4px 0 0 8px;border-radius:3px}
  .service-sub{position:absolute;left:33px;top:66px;font-size:16px;color:#444}
  .service-copy{position:absolute;left:33px;top:105px;width:416px;font-size:12px;line-height:19px;color:#444;text-align:justify;hyphens:auto}
  .benefits-title{position:absolute;left:33px;top:211px;width:400px;font-size:14.5px;line-height:18px;font-weight:700;color:#444}
  .benefits{position:absolute;left:33px;top:258px;width:420px;list-style:none;font-size:13px}
  .benefits li{display:flex;margin-bottom:10px}
  .benefits svg{flex:none;margin:2px 6px 0 0}
  .benefits .label{width:168px;color:#333}
  .benefits .detail{width:220px;font-size:11.5px;line-height:14px;color:#666}
  .partners-bar{position:absolute;left:25px;top:410px;width:262px;height:24px;background:var(--blue);color:#fff;font-weight:700;font-size:15px;padding:3px 0 0 9px;border-radius:0 3px 3px 0}
  .partner-row{position:absolute;left:0;top:442px;width:475px;height:60px;background:#fff;display:flex;align-items:center;justify-content:space-around;padding:0 20px}
  .badge{background:var(--badge-grey)}
  .badge--wide{width:80px;height:26px;border-radius:3px}
  .badge--tile{width:50px;height:55px;background:#3f9de0;border-radius:2px}
  .badge--red{width:80px;height:20px;background:#e84a4a;border-radius:3px}
  .badge--round{width:30px;height:30px;border-radius:50%;background:#9aa0a6}
</style>
</head>
<body>

<article class="flyer flyer--front">
  <div class="hero-photo" role="img" aria-label="Photo of a businessman in a suit writing service names in sketched clouds on a glass board"></div>

  <div class="brand"><span class="brand__dot"></span><span class="brand__name">FRT</span></div>

  <span class="tab" style="top:106px"></span>
  <h2 class="section-title" style="top:104px">Who Are We?</h2>
  <p class="section-copy" style="top:131px"><strong>Fern Ridge Technology</strong> is your partner in both affordable Computer Support and the worthwhile achievements of your business. With personalized Network Services, you can get best-fit solutions at competitive prices.</p>

  <span class="tab" style="top:272px"></span>
  <h2 class="section-title" style="top:271px">What We Do?</h2>
  <p class="section-copy" style="top:298px">With IT Services and solutions from FRT, you can finally enjoy the advantages of your business technology. Our experts will simplify the technology you rely on every day, so you can get back to business.</p>

  <div class="cta">Change Your Outlook on<br><strong>Business IT</strong></div>

  <div class="url-strip">
    <svg width="475" height="22" aria-hidden="true"><polygon points="0,0 230,0 250,22 0,22" fill="var(--strip)"/><polyline points="230,2 250,20 475,20" fill="none" stroke="#777" stroke-width="2"/></svg>
    <span class="url">www.fernridgetech.com</span>
  </div>
  <footer class="footer">
    <p class="footer__tagline">We take care of technology so you can focus on your business.</p>
    <span class="footer__rule"></span>
    <div class="footer__contact">
      <p class="footer__company">Fern Ridge Technology, Inc.</p>
      <p>480 Meadowlark Ave.</p><p>Suite 210</p><p>Linden Falls, IL 60999</p>
      <p class="footer__phone">Phone: 555-014-2278 | Fax: 555-014-3391</p>
    </div>
  </footer>
</article>

<article class="flyer flyer--back">
  <div class="hero-photo hero-photo--faint" role="img" aria-label="Faint background photo of a businessman with sketched service clouds"></div>
  <h2 class="service-bar">Managed Services</h2>
  <p class="service-sub">Stop waiting for your technology to break</p>
  <p class="service-copy">When something goes wrong with your IT, everything grinds to a halt. With a standard break/fix service contract, you have to wait for something to break before your provider can fix it. That equation seems to make sense – even though it could easily result in hours of downtime. But what if you could keep your IT from breaking in the first place?</p>
  <h3 class="benefits-title">With managed services from Fern Ridge Technology, you can expect:</h3>
  <ul class="benefits">
    <li><svg width="13" height="12" viewBox="0 0 13 12"><path d="M1 6 L5 10 L12 1" fill="none" stroke="var(--blue)" stroke-width="2"/></svg><span class="label">Peace of mind</span><span class="detail">your systems are monitored 24/7</span></li>
    <li><svg width="13" height="12" viewBox="0 0 13 12"><path d="M1 6 L5 10 L12 1" fill="none" stroke="var(--blue)" stroke-width="2"/></svg><span class="label">Less downtime</span><span class="detail">we identify and fix issues before they cause problems</span></li>
    <li><svg width="13" height="12" viewBox="0 0 13 12"><path d="M1 6 L5 10 L12 1" fill="none" stroke="var(--blue)" stroke-width="2"/></svg><span class="label">Fewer disruptions</span><span class="detail">we provide most services remotely or overnight</span></li>
    <li><svg width="13" height="12" viewBox="0 0 13 12"><path d="M1 6 L5 10 L12 1" fill="none" stroke="var(--blue)" stroke-width="2"/></svg><span class="label">Predictable budgeting</span><span class="detail">all-inclusive, all-you-can-use, flat-rate IT services that include hardware and software.</span></li>
  </ul>
  <h3 class="partners-bar">Our Partners &amp; Certifications:</h3>
  <div class="partner-row">
    <span class="badge badge--wide"></span>
    <span class="badge badge--tile"></span>
    <span class="badge badge--red"></span>
    <span class="badge badge--round"></span>
  </div>
  <div class="url-strip">
    <svg width="475" height="22" aria-hidden="true"><polygon points="245,0 475,0 475,22 225,22" fill="var(--strip)"/><polyline points="0,20 225,20 245,2" fill="none" stroke="#777" stroke-width="2"/></svg>
    <span class="url">www.fernridgetech.com</span>
  </div>
  <footer class="footer">
    <p class="footer__tagline">We take care of technology so you can focus on your business.</p>
    <span class="footer__rule"></span>
    <div class="footer__contact">
      <p class="footer__company">Fern Ridge Technology, Inc.</p>
      <p>480 Meadowlark Ave.</p><p>Suite 210</p><p>Linden Falls, IL 60999</p>
      <p class="footer__phone">Phone: 555-014-2278 | Fax: 555-014-3391</p>
    </div>
  </footer>
</article>

</body>
</html>
```